BKA

Please send us some options for letterhead I attached our Logo. In addition to the Logo we need this information somewhere on the page

47 Fenbury Lane
Brookhaven, CT 06412
203-481-7629

```html
<!DOCTYPE html>
<html lang="en">
<head>
<meta charset="utf-8">
<title>BKA Letterhead</title>
<link href="https://fonts.googleapis.com/css2?family=Arimo:ital,wght@0,700;1,700&display=swap" rel="stylesheet">
<style>
  :root {
    --brand-blue: #1a7cc4;
    --brand-blue-light: #8fd0f2;
    --brand-brown: #554541;
    --brand-grey: #8a8a8a;
    --watermark: #efeeed;
    --paper: #ffffff;
    --ink: #111111;
  }
  html, body {
    margin: 0;
    padding: 0;
    overflow: hidden;
    background: var(--paper);
  }
  .letterhead {
    position: relative;
    width: 848px;
    height: 1200px;
    overflow: hidden;
    background: var(--paper);
    font-family: "Arimo", Arial, sans-serif;
  }
  .letterhead__frame {
    position: absolute;
    inset: 0;
  }
  .letterhead__brand {
    position: absolute;
    top: 60px;
    left: 470px;
    display: flex;
    align-items: center;
    gap: 18px;
  }
  .letterhead__brand-mark {
    width: 40px;
    height: 40px;
    background: var(--brand-brown);
  }
  .letterhead__brand-name {
    margin: 0;
    font-size: 78px;
    font-weight: 700;
    letter-spacing: 3px;
    line-height: 1;
    color: var(--brand-grey);
  }
  .letterhead__watermark {
    position: absolute;
    top: 470px;
    left: 0;
    width: 848px;
    text-align: center;
    font-size: 300px;
    font-weight: 700;
    line-height: 1;
    letter-spacing: 8px;
    color: var(--watermark);
    user-select: none;
  }
  .letterhead__contact {
    position: absolute;
    left: 71px;
    top: 1126px;
    font-size: 18px;
    font-weight: 700;
    line-height: 1.25;
    color: var(--ink);
  }
  .letterhead__contact p { margin: 0; }
  .letterhead__phone { font-style: italic; }
</style>
</head>
<body>
<div class="letterhead">
  <svg class="letterhead__frame" width="848" height="1200" viewBox="0 0 848 1200" aria-hidden="true">
    <defs>
      <radialGradient id="glow-top" cx="0.45" cy="0.3" r="0.7">
        <stop offset="0" stop-color="#8fd0f2"/>
        <stop offset="1" stop-color="#1a7cc4"/>
      </radialGradient>
      <radialGradient id="glow-bottom" cx="0.6" cy="0.85" r="0.7">
        <stop offset="0" stop-color="#8fd0f2"/>
        <stop offset="1" stop-color="#1a7cc4"/>
      </radialGradient>
    </defs>
    <path class="swoosh swoosh--brown" d="M0 0 H400 C230 30 45 150 0 325 Z" fill="#554541"/>
    <path class="swoosh swoosh--blue" d="M0 0 H385 C245 20 55 125 0 285 Z" fill="url(#glow-top)"/>
    <path class="swoosh swoosh--brown" d="M848 845 C830 1030 660 1170 456 1200 H848 Z" fill="#554541"/>
    <path class="swoosh swoosh--blue" d="M848 975 C815 1090 700 1170 570 1200 H848 Z" fill="url(#glow-bottom)"/>
  </svg>

  <header class="letterhead__brand">
    <span class="letterhead__brand-mark"></span>
    <h1 class="letterhead__brand-name">BKA</h1>
  </header>

  <div class="letterhead__watermark" aria-hidden="true">BKA</div>

  <footer class="letterhead__contact">
    <p class="letterhead__address">47 Fenbury Lane Brookhaven, CT 06412</p>
    <p class="letterhead__phone">203-481-7629</p>
  </footer>
</div>
</body>
</html>
```